Love Your Hearing - Life Sounds Good

I need a website. I had a company doing it, and it looked very nice, but they went way up on hosting costs and said they owned the design of the site. I changed hosts to keep costs down. You can see the current design at crestvaleaudio.com. They said I could use the copy and images from the current website. So you could cut and paste to speed things up. My logo and other images are on the current website. If you are unable to use I can send other digital copies.

Target Market(s)

seniors 55 and up

Number of Pages Required

4 page

Font styles to use
Sans Serif

Colors
0255a3
f78f20

Requirements
Must have
• Video testimonies that I can add without assistance. I use youtube links for the videos.
Nice to have
• The color scheme theme can be drawn from the logo, which is on the current webstie crestvaleaudio.com
Should not have
• Should not have anything related to SonoPath on the website.

```html
<!DOCTYPE html>
<html lang="en">
<head>
<meta charset="utf-8">
<title>Crestvale Hearing Center – Home</title>
<link href="https://fonts.googleapis.com/css2?family=Lora:wght@400;700&family=Open+Sans:wght@400;600;700&display=swap" rel="stylesheet">
<style>
:root{
  --blue:#0a4f9c;
  --blue-dark:#083f80;
  --orange:#f78f20;
  --ink:#333;
  --muted:#666;
  --card:#f2f2f2;
  --white:#fff;
  --serif:'Lora', Georgia, serif;
  --sans:'Open Sans', Arial, sans-serif;
}
*{box-sizing:border-box;margin:0;padding:0}
html,body{width:1200px;height:4063px;overflow:hidden}
body{font-family:var(--sans);color:var(--ink);background:var(--white);font-size:14px;line-height:1.5}
.wrap{width:1040px;margin:0 auto;position:relative}
.btn{display:inline-block;background:var(--orange);color:var(--white);font-family:var(--sans);font-size:13px;font-weight:600;padding:8px 28px;border-radius:3px;text-decoration:none}
.section-title{font-family:var(--serif);font-size:32px;font-weight:400;text-align:center}

/* header */
.top{height:108px}
.top .wrap{display:flex;align-items:center;height:108px;justify-content:space-between}
.logo{display:flex;align-items:center;gap:12px}
.logo-mark{width:40px;height:40px;background:var(--orange);border-radius:4px;flex-shrink:0}
.logo-name{font-family:var(--serif);font-weight:700;font-size:26px;color:var(--blue);line-height:1}
.info{display:flex;align-items:center;gap:36px;font-size:12px;color:var(--ink)}
.info-item{display:flex;align-items:center;gap:8px;line-height:1.35}
.info-item b{color:var(--blue)}
.social{display:flex;gap:8px}
.social span{width:24px;height:24px;border-radius:50%;background:var(--blue)}
.social span:nth-child(2){background:var(--orange)}
.nav{background:var(--blue);height:44px}
.nav ul{list-style:none;display:flex;align-items:center;height:44px;justify-content:space-between}
.nav li{color:var(--white);font-size:14px;font-weight:600;padding:0 24px;height:44px;line-height:44px}
.nav li.active{background:var(--orange)}
.nav li.cta{background:var(--orange);height:30px;line-height:30px;border-radius:3px}

/* hero */
.hero{height:485px;position:relative;background:linear-gradient(100deg,#c9a48f 0%,#e6d6cc 35%,#eef1f3 60%,#f4f5f6 100%)}
.hero-text{position:absolute;left:720px;top:105px;width:380px;text-align:center}
.hero-text .kicker{font-family:var(--serif);font-size:24px}
.hero-text h1{font-family:var(--serif);font-weight:400;font-size:42px;line-height:1.15}
.hero-text p{font-size:14px;margin:6px 0 14px}
.arrow{position:absolute;top:50%;width:30px;height:30px;margin-top:-15px}
.arrow.l{left:14px}.arrow.r{right:14px}
.dots{position:absolute;left:596px;bottom:36px;display:flex;gap:6px}
.dots span{width:8px;height:8px;background:var(--blue);border-radius:50%}

/* about */
.about{height:455px}
.about .wrap{display:flex;justify-content:space-between;padding-top:66px}
.about-text{width:500px}
.about-text h2{font-family:var(--serif);font-size:38px;font-weight:400;position:relative;padding-bottom:10px;margin-bottom:18px}
.about-text h2::after{content:"";position:absolute;left:0;bottom:0;width:60px;height:3px;background:var(--orange)}
.about-text p{font-size:14px;line-height:1.45;margin-bottom:14px;color:var(--ink)}
.about .btn{margin-top:14px}
.video{width:502px;height:303px;margin-top:7px;background:linear-gradient(135deg,#3c4f63,#8a96a0);position:relative}
.video svg{position:absolute;left:219px;top:120px}
.video-bar{position:absolute;left:0;right:0;bottom:0;height:26px;background:rgba(0,0,0,.55)}

/* services */
.services{background:var(--blue);height:696px;padding-top:56px;color:var(--white)}
.service-grid{display:grid;grid-template-columns:repeat(3,304px);gap:29px 30px;justify-content:center;margin-top:20px}
.service{background:var(--white);color:var(--ink);height:221px;text-align:center;padding:36px 26px 0;border-radius:2px}
.service.featured{background:var(--orange);color:var(--white)}
.service h3{font-family:var(--serif);font-weight:400;font-size:20px;margin:12px 0 8px}
.service p{font-size:13px;line-height:1.4}
.center-btn{text-align:center;margin-top:38px}

/* features */
.features{height:509px;padding-top:68px}
.card-row{display:flex;justify-content:space-between}
.feature{width:320px;background:var(--card);height:392px;text-align:center}
.feature .photo{height:197px}
.feature h3{font-family:var(--serif);font-weight:400;font-size:22px;margin:28px 0 10px}
.feature p{font-size:13px;line-height:1.4;padding:0 44px;margin-bottom:18px}

/* testimonials */
.testimonials{background:var(--blue);height:515px;color:var(--white);padding-top:46px;position:relative;text-align:center}
.testimonials .sub{font-size:14px}
.t-row{display:flex;justify-content:space-between;margin-top:30px}
.t-card{width:504px;height:236px;background:var(--white);display:flex;text-align:left;color:var(--ink);border-radius:3px;overflow:hidden}
.t-card .photo{width:230px;flex-shrink:0;position:relative}
.t-card .photo svg{position:absolute;left:91px;top:94px}
.t-body{padding:36px 24px;flex:1}
.t-body h4{font-family:var(--serif);font-size:17px;font-weight:400;letter-spacing:.5px}
.t-body .role{color:var(--blue);font-size:13px}
.stars{color:var(--orange);font-size:15px;letter-spacing:2px;margin:2px 0 6px}
.t-body p{font-size:12.5px;line-height:1.35}
.testimonials .arrow{top:280px}

/* info */
.info-cards{height:580px;padding-top:52px}
.info-card{width:320px;text-align:center}
.info-card h3{font-family:var(--serif);font-weight:700;font-size:24px;line-height:1.3;height:72px;margin-bottom:16px;padding:0 34px;display:flex;align-items:flex-start;justify-content:center}
.info-card .body{background:var(--card);height:368px}
.info-card .photo{height:206px}
.info-card p{font-size:13px;line-height:1.4;padding:24px 34px 12px;height:104px}

/* contact strip */
.strip{display:flex;height:306px}
.help{width:601px;background:var(--blue);color:var(--white);padding:68px 0 0 81px}
.help h2,.news h2{font-family:var(--serif);font-weight:400;font-size:28px}
.help .rule{width:130px;height:2px;background:var(--orange);margin:14px 0 18px}
.help .line{font-size:14px;display:flex;gap:12px;align-items:center;margin-top:2px}
.help .line.phone{font-size:24px;font-weight:700;color:var(--orange);margin-bottom:4px}
.help .line span.i{color:var(--orange);width:14px;font-size:14px}
.news{flex:1;background:var(--orange);color:var(--white);padding:62px 0 0 66px}
.news p{font-size:14px;font-weight:600;width:470px;margin-top:10px;line-height:1.45}
.email-field{margin-top:18px;width:470px;height:54px;background:var(--white);border-radius:27px;position:relative;color:var(--muted);font-size:14px;padding:16px 26px}
.email-field .send{position:absolute;right:8px;top:7px;width:40px;height:40px;border-radius:50%;background:var(--blue)}

/* footer */
.footer{height:306px;padding-top:48px}
.footer .wrap{display:flex}
.f-col h4{font-family:var(--serif);font-weight:400;font-size:17px;margin-bottom:14px}
.f-col ul{list-style:none;font-size:13px;line-height:1.85}
.f-col ul li::before{content:"›";color:var(--orange);margin-right:8px}
.f-about{width:293px}
.f-about .logo-name{font-size:22px}
.f-about p{font-size:12.5px;line-height:1.45;margin:14px 0 8px;width:220px}
.f-social{display:flex;gap:8px;margin-top:10px}
.f-social span{width:26px;height:26px;border-radius:50%;background:var(--orange)}
.f-links{width:203px}
.f-areas{width:255px}
.f-form{width:289px}
.fields{display:flex;gap:4px}
.field{border:1px solid #ccc;height:26px;font-size:11px;padding:4px 6px;color:var(--muted);flex:1}
.field.msg{height:66px;margin-top:6px}
.f-form .btn{margin:12px 0 0 60px;border-radius:14px;padding:5px 36px}
.bottom{height:59px;border-top:1px solid #e2e2e2}
.bottom .wrap{display:flex;justify-content:space-between;align-items:center;height:58px;font-size:12px;color:var(--muted)}
.cards{display:flex;gap:8px}
.cards span{width:40px;height:24px;border:1px solid #ccc;background:#f4f4f4;border-radius:2px}
</style>
</head>
<body>

<header class="top">
  <div class="wrap">
    <div class="logo"><span class="logo-mark"></span><span class="logo-name">Crestvale Hearing Center</span></div>
    <div class="info">
      <div class="info-item">
        <svg width="22" height="22" viewBox="0 0 24 24"><path d="M12 2a7 7 0 0 0-7 7c0 5 7 13 7 13s7-8 7-13a7 7 0 0 0-7-7zm0 9.5A2.5 2.5 0 1 1 12 6.5a2.5 2.5 0 0 1 0 5z" fill="#0a4f9c"/></svg>
        <span>410 W. Elm St, Suite<br>210, Crestvale, NC 28099</span>
      </div>
      <div class="info-item">
        <svg width="22" height="22" viewBox="0 0 24 24"><circle cx="12" cy="12" r="11" fill="none" stroke="#0a4f9c" stroke-width="2"/><path d="M8 7l2 0 1 3-1.5 1a7 7 0 0 0 3.5 3.5l1-1.5 3 1v2a1 1 0 0 1-1 1A9 9 0 0 1 7 8a1 1 0 0 1 1-1z" fill="#0a4f9c"/></svg>
        <span><b>Call us Now!</b><br>00 123 456 7890</span>
      </div>
      <div class="social"><span></span><span></span><span></span><span></span></div>
    </div>
  </div>
</header>

<nav class="nav">
  <div class="wrap">
    <ul>
      <li class="active">Home</li><li>About us</li><li>Hearing Aids</li><li>Services ▾</li><li>Education</li><li>Contact us</li><li class="cta">Appointment</li>
    </ul>
  </div>
</nav>

<section class="hero" role="img" aria-label="Smiling senior couple sitting on a beach, with a row of hearing aid models">
  <div class="hero-text">
    <div class="kicker">Recapture</div>
    <h1>The Sounds Of Life</h1>
    <p>and the intimacy of a quiet conversation</p>
    <span class="btn">Read More</span>
  </div>
  <svg class="arrow l" viewBox="0 0 30 30"><path d="M19 5L9 15l10 10" fill="none" stroke="#555" stroke-width="3"/></svg>
  <svg class="arrow r" viewBox="0 0 30 30"><path d="M11 5l10 10-10 10" fill="none" stroke="#555" stroke-width="3"/></svg>
  <div class="dots"><span></span><span></span><span></span></div>
</section>

<section class="about">
  <div class="wrap">
    <div class="about-text">
      <h2>About us</h2>
      <p>"I was first introduced to hearing aids as a patient. At the tender age of 36, I was diagnosed with profound hearing loss by a hearing healthcare provider in Raleigh, North Carolina.</p>
      <p>I was fitted with two in-the-ear hearing aids that instantly changed my life! There was no more straining to hear what people were saying, and no more trying to piece together a discussion to make sense of the conversation.</p>
      <p>Now I could relax and enjoy the pleasant sounds of music and conversation. I actually had more confidence and energy at the end of the work day.</p>
      <span class="btn">Read More</span>
    </div>
    <div class="video" role="img" aria-label="Video still of the practice owner speaking in his office">
      <svg width="64" height="64" viewBox="0 0 64 64"><circle cx="32" cy="32" r="30" fill="rgba(0,0,0,.6)"/><path d="M26 20l18 12-18 12z" fill="#fff"/></svg>
      <div class="video-bar"></div>
    </div>
  </div>
</section>

<section class="services">
  <h2 class="section-title">Our Services</h2>
  <div class="service-grid">
    <div class="service">
      <svg width="40" height="40" viewBox="0 0 40 40"><path d="M14 28c0-6 10-6 10-14a7 7 0 0 0-14 0" fill="none" stroke="#f78f20" stroke-width="3"/><path d="M28 12a9 9 0 0 1 0 14M32 8a14 14 0 0 1 0 22" fill="none" stroke="#f78f20" stroke-width="2.5"/></svg>
      <h3>Hearing Evaluations</h3><p>Lorem Ipsum is simply dummy and text of the printing and typesetting in the industry.</p>
    </div>
    <div class="service featured">
      <svg width="40" height="40" viewBox="0 0 40 40"><path d="M8 32l14-14M22 18l8-8 4 4-8 8z" fill="none" stroke="#fff" stroke-width="3"/></svg>
      <h3>Video Otoscopy</h3><p>Lorem Ipsum is simply dummy and text of the printing and typesetting in the industry.</p>
    </div>
    <div class="service">
      <svg width="40" height="40" viewBox="0 0 40 40"><path d="M13 16a8 8 0 0 1 16 0c0 7-8 8-8 15a4 4 0 0 1-7 1" fill="none" stroke="#f78f20" stroke-width="3"/></svg>
      <h3>Hearing Aid Fitting</h3><p>Lorem Ipsum is simply dummy and text of the printing and typesetting in the industry.</p>
    </div>
    <div class="service">
      <svg width="40" height="40" viewBox="0 0 40 40"><path d="M12 24c0-10 16-14 18-4 1 6-6 8-10 12" fill="none" stroke="#f78f20" stroke-width="3"/><circle cx="12" cy="28" r="3" fill="#f78f20"/></svg>
      <h3>Follow Up Service</h3><p>Lorem Ipsum is simply dummy and text of the printing and typesetting in the industry.</p>
    </div>
    <div class="service">
      <svg width="40" height="40" viewBox="0 0 40 40"><path d="M12 10h16v12a8 8 0 0 1-16 0z" fill="none" stroke="#f78f20" stroke-width="3"/><path d="M20 30v6" stroke="#f78f20" stroke-width="3"/></svg>
      <h3>Ear Molds</h3><p>Lorem Ipsum is simply dummy and text of the printing and typesetting in the industry.</p>
    </div>
    <div class="service">
      <svg width="40" height="40" viewBox="0 0 40 40"><path d="M10 30c0-8 12-8 12-16a6 6 0 0 0-12 0" fill="none" stroke="#f78f20" stroke-width="3"/><path d="M26 10a8 8 0 0 1 4 6M28 4a14 14 0 0 1 7 12" fill="none" stroke="#f78f20" stroke-width="2.5"/></svg>
      <h3>Wireless Technology</h3><p>Lorem Ipsum is simply dummy and text of the printing and typesetting in the industry.</p>
    </div>
  </div>
  <div class="center-btn"><span class="btn">View More</span></div>
</section>

<section class="features">
  <div class="wrap card-row">
    <div class="feature">
      <div class="photo" role="img" aria-label="Audiologist examining a senior man's ear" style="background:linear-gradient(135deg,#d9d0c7,#a9a39d)"></div>
      <h3>Hearing Aids</h3><p>Lorem Ipsum is simply dummy and text of the printing and typesetting in the industry.</p><span class="btn">View More</span>
    </div>
    <div class="feature">
      <div class="photo" role="img" aria-label="Man holding his head in discomfort from ringing ears" style="background:linear-gradient(135deg,#8fb6d6,#5e88ad)"></div>
      <h3>Tinnitus Treatment</h3><p>Lorem Ipsum is simply dummy and text of the printing and typesetting in the industry.</p><span class="btn">View More</span>
    </div>
    <div class="feature">
      <div class="photo" role="img" aria-label="Close view of a hearing aid being placed behind an ear" style="background:linear-gradient(135deg,#e9c6b0,#c9967a)"></div>
      <h3>Ear Molds (Protection)</h3><p>Lorem Ipsum is simply dummy and text of the printing and typesetting in the industry.</p><span class="btn">View More</span>
    </div>
  </div>
</section>

<section class="testimonials">
  <h2 class="section-title">Video Testimonials</h2>
  <p class="sub">Lorem Ipsum is simply dummy and text of the printing.</p>
  <div class="wrap t-row">
    <div class="t-card">
      <div class="photo" role="img" aria-label="Video still of a patient sharing his experience" style="background:linear-gradient(135deg,#6d6a86,#3e3b55)">
        <svg width="48" height="48" viewBox="0 0 48 48"><circle cx="24" cy="24" r="22" fill="rgba(0,0,0,.55)" stroke="#fff" stroke-width="2"/><path d="M19 15l14 9-14 9z" fill="#fff"/></svg>
      </div>
      <div class="t-body"><h4>WALTER PRYOR</h4><div class="role">Creative Director</div><div class="stars">★★★★★</div><p>“ Lorem Ipsum simply dummy text printingand typesetting industry simply dummy apsum is simply dummy ”</p></div>
    </div>
    <div class="t-card">
      <div class="photo" role="img" aria-label="Video still of a patient sharing his experience" style="background:linear-gradient(135deg,#8f8a80,#5a564f)">
        <svg width="48" height="48" viewBox="0 0 48 48"><circle cx="24" cy="24" r="22" fill="rgba(0,0,0,.55)" stroke="#fff" stroke-width="2"/><path d="M19 15l14 9-14 9z" fill="#fff"/></svg>
      </div>
      <div class="t-body"><h4>Dale Morrow</h4><div class="role">Creative Director</div><div class="stars">★★★★★</div><p>“ Lorem Ipsum simply dummy text printingand typesetting industry simply dummy apsum is simply dummy ”</p></div>
    </div>
  </div>
  <div class="center-btn"><span class="btn">View More</span></div>
  <svg class="arrow l" viewBox="0 0 30 30"><path d="M19 5L9 15l10 10" fill="none" stroke="#fff" stroke-width="3"/></svg>
  <svg class="arrow r" viewBox="0 0 30 30"><path d="M11 5l10 10-10 10" fill="none" stroke="#fff" stroke-width="3"/></svg>
</section>

<section class="info-cards">
  <div class="wrap card-row">
    <div class="info-card">
      <h3>Symptoms of Hearing Loss</h3>
      <div class="body">
        <div class="photo" role="img" aria-label="Hand cupped behind an ear with sound wave rings" style="background:linear-gradient(135deg,#4a6b73,#b9c7c4)"></div>
        <p>Hearing loss increases over time and can gounnoticed for years, so it's important to be aware of the symptoms</p>
        <span class="btn">View More</span>
      </div>
    </div>
    <div class="info-card">
      <h3>Benefits of Hearing Aids</h3>
      <div class="body">
        <div class="photo" role="img" aria-label="Young woman touching her ear against a light background" style="background:linear-gradient(135deg,#f1e2d8,#cf9c84)"></div>
        <p>With the medical and technological advances in hearing healthcare, nearly all hearing disabilities are treatable.</p>
        <span class="btn">View More</span>
      </div>
    </div>
    <div class="info-card">
      <h3>Did You Know?</h3>
      <div class="body">
        <div class="photo" role="img" aria-label="Man with glasses looking at his phone" style="background:linear-gradient(135deg,#e7e9eb,#9fa8b0)"></div>
        <p>Cognitive impacts, such as poor memory and decreased ability to learn new tasks, could be related to hearing loss.</p>
        <span class="btn">View More</span>
      </div>
    </div>
  </div>
</section>

<section class="strip">
  <div class="help">
    <h2>Need Help?</h2>
    <div class="rule"></div>
    <div class="line phone"><span class="i">☎</span><span>: (704) 555-0148</span></div>
    <div class="line"><span class="i">◷</span><span>: 8:00 to 5:00 Monday through Friday</span></div>
    <div class="line"><span class="i">✉</span><span>: Contact@crestvaleaudio.com</span></div>
  </div>
  <div class="news">
    <h2>Newsletter Signup</h2>
    <p>Please subscribe and receive our latest news, promotions, events, and clinic updates you can't get anywhere else.</p>
    <div class="email-field">Enter your email here*
      <span class="send"><svg width="40" height="40" viewBox="0 0 40 40"><path d="M12 20l16-7-6 16-3-6z" fill="#fff"/></svg></span>
    </div>
  </div>
</section>

<footer class="footer">
  <div class="wrap">
    <div class="f-col f-about">
      <div class="logo"><span class="logo-mark" style="width:30px;height:30px"></span><span class="logo-name">Crestvale Hearing</span></div>
      <p>Lorem Ipsum is simply dummy text of the printing and typesetting Aids and in the industry.</p>
      <div style="font-size:12.5px">Read More ›</div>
      <div class="f-social"><span></span><span></span><span></span><span></span><span></span></div>
    </div>
    <div class="f-col f-links">
      <h4>Quick Link</h4>
      <ul><li>Home</li><li>About us</li><li>Hearing Aids</li><li>Services</li><li>Education</li><li>Tips</li><li>Contact us</li></ul>
    </div>
    <div class="f-col f-areas">
      <h4>Healthcare Services</h4>
      <ul><li>Gaston County</li><li>Gastonia</li><li>Stanley</li><li>Dallas</li><li>Cramerton</li><li>Lowell</li><li>other</li></ul>
    </div>
    <div class="f-col f-form">
      <h4>Contact us</h4>
      <div class="fields"><div class="field">Name</div><div class="field">Email</div><div class="field">Phone</div></div>
      <div class="field msg">Message</div>
      <span class="btn">Send</span>
    </div>
  </div>
</footer>

<div class="bottom">
  <div class="wrap">
    <span>CopyRight © 2019 Crestvale Hearing Center. All Right Reserve</span>
    <div class="cards"><span></span><span></span><span></span><span></span></div>
  </div>
</div>

</body>
</html>
```